Lantern Square, Steady Course. (Website Design)

We are launching a new bipartisan civic movement: Lantern Square. Steady Course.
The mission is this: Americans deserve a government that is legally required to serve them honestly.
We are looking for a world-class website designer capable of creating an emotionally powerful, modern, cinematic landing page experience that feels larger than politics.
This is not a campaign website for a political party or candidate. We are not looking for a red, white, and blue page with stripes, or American flags, or stock footage of smiling people in a voting booth. We are looking for an emotional and cinematic experience through and through.
The visual direction should feel:
Historic
Hopeful
American
Emotional
Cinematic
Trustworthy
Timeless
The goal is to make visitors feel that they are witnessing the beginning of something important and want to be part of it in the end.
Primary Objective:
Inspire visitors to participate in a one-minute survey and cast their vote.
The survey itself is extremely short and takes approximately one minute to complete.
Everything on the page should ultimately guide visitors toward this action while creating enough curiosity, trust, emotional engagement, and excitement that they feel compelled to take part in the movement.
Audience:
The audience is ordinary Americans across the political spectrum: Democrats, Republicans, Independents.
The design should feel unifying and welcoming.
It should avoid looking partisan, ideological, activist, or government-issued.
Creative Freedom:
We are intentionally giving designers substantial creative freedom.
We are not looking for someone to simply arrange content into predefined sections.
Instead, we are looking for a designer who can think strategically about user experience and persuasion.
The ideal design is as minimal as possible, but you may always:
Use as many sections as you believe are necessary.
Use as many images as you believe are necessary.
Include storytelling elements.
Include data visualizations.
Include timelines.
Include videos.
Include animations.
Include or exclude sections as you see fit.
Reorganize the flow entirely.
We uploaded some files containing text and section suggestions. You don’t have to use them.
We also uploaded some images to convey the general feel we’re looking for.
We are much more interested in the effectiveness of the overall experience than in any specific layout.
What success looks like:
Think outside the box.
Please do not create another generic political website. We have already explored those approaches.
We are looking for something different.
The winning design will be the one that most effectively guides visitors from curiosity to belief to participation.
When a visitor reaches the end of the experience, they should feel:
This is bigger than politics.
This is something I can support regardless of party.
This feels credible.
This feels hopeful.
I want to be part of this.
Use the survey results, the research findings, the principles, the storytelling, or any other elements you believe will help build trust and inspire participation.
Don't just impress us with flashy visuals. Impress us with a website experience that inspires people to become part of the movement and cast their vote.
The final call-to-action should feel like the natural conclusion of the journey, not a request for engagement.
Our goal is not simply to inform visitors. Our goal is to inspire them to cast their vote.
Prioritize emotional impact, storytelling, clarity, and persuasion over decorative design elements.
Final words:
Design a website experience that successfully inspires visitors to take the survey and cast their vote.
Think like a storyteller, not just a designer.
Thank you for your interest in the project.
Best of luck.

```html
<!DOCTYPE html>
<html lang="en">
<head>
<meta charset="utf-8">
<title>Lantern Square. Steady Course.</title>
<link href="https://fonts.googleapis.com/css2?family=Playfair+Display:ital,wght@0,400;1,400&family=Plus+Jakarta+Sans:wght@400;600;700&display=swap" rel="stylesheet">
<style>
:root{
  --cream:#f7f6ee;
  --gold:#b3ac74;
  --ink:#111111;
  --white:#ffffff;
  --night:#050505;
  --muted:#9a9a9a;
}
*{margin:0;padding:0;box-sizing:border-box}
html,body{width:1200px;height:2267px;overflow:hidden;background:var(--night)}
body{position:relative;font-family:"Plus Jakarta Sans",sans-serif;color:var(--ink)}
.serif{font-family:"Playfair Display",serif;font-weight:400}
.gold{color:var(--gold)}
em{font-style:italic}
.abs{position:absolute}

/* section rail */
.rail{position:absolute;left:20px;width:6px;display:flex;flex-direction:column;align-items:center;gap:6px}
.rail span{width:4px;height:4px;border-radius:50%;background:#b9b9b9}
.rail span.on{height:18px;border-radius:2px;background:var(--gold)}

/* hero */
.hero{position:absolute;left:0;top:0;width:1200px;height:667px}
.hero-panel{position:absolute;left:0;top:0;width:600px;height:667px;background:var(--cream)}
.hero-title{left:173px;top:90px;font-size:41px;line-height:48px}
.counter{left:173px;top:562px;font-size:34px}
.counter .total{color:var(--muted)}
.arrow{position:absolute;top:574px;width:27px;height:27px;display:flex;align-items:center;justify-content:center}
.arrow.prev{left:461px;background:#e9e8de}
.arrow.next{left:494px;background:var(--ink)}
.hero-photo{position:absolute;left:600px;top:0;width:600px;height:667px;
  background:linear-gradient(180deg,#dfe1e4 0%,#c6c8cc 30%,#8a6f6c 55%,#4c3535 78%,#2a2222 100%)}
.hero-photo::after{content:"";position:absolute;inset:0;background:radial-gradient(ellipse at 45% 40%,rgba(200,40,50,.35),transparent 55%)}
.numeral{position:absolute;right:70px;top:40px;font-size:150px;color:rgba(60,60,60,.35);z-index:1}
.quote{position:absolute;left:676px;top:508px;width:370px;font-size:24px;line-height:32px;color:var(--white);z-index:1}

/* survey */
.survey{position:absolute;left:0;top:667px;width:1200px;height:666px;background:var(--white);overflow:hidden}
.survey-title{left:173px;top:86px;font-size:41px}
.stats{position:absolute;left:604px;top:88px;width:440px;font-size:15.5px;line-height:24px}
.stat{font-size:41px;line-height:48px;color:var(--gold)}
.stats p{margin:0}
.note{font-size:7px;margin:10px 0 22px}
.rule{width:62px;height:1px;background:var(--ink);margin:26px 0 26px}
.fade{position:absolute;left:0;bottom:0;width:100%;height:40px;background:linear-gradient(rgba(255,255,255,0),#fff)}

/* history */
.history{position:absolute;left:0;top:1333px;width:1200px;height:567px;
  background:radial-gradient(ellipse at 55% 35%,#2b2d30 0%,#15161a 45%,#060606 85%)}
.history-title{position:absolute;left:0;top:120px;width:1200px;text-align:center;font-size:41px;color:var(--white)}
.history-copy{position:absolute;left:230px;top:210px;width:740px;text-align:center;font-size:16.5px;line-height:24px;color:var(--white)}
.history-line{position:absolute;left:0;top:277px;width:1200px;text-align:center;font-size:20px;color:var(--gold)}
.history-close{position:absolute;left:0;top:331px;width:1200px;text-align:center;font-size:16px;color:var(--white)}
.vote-btn{position:absolute;left:533px;top:397px;width:133px;height:46px;background:var(--gold);color:var(--ink);
  font-size:16px;font-weight:600;display:flex;align-items:center;justify-content:center}

/* strip */
.strip{position:absolute;left:0;top:1900px;width:1200px;height:100px;display:flex}
.strip div{flex:1}

/* footer */
.footer{position:absolute;left:0;top:2000px;width:1200px;height:267px;background:var(--night);color:var(--white)}
.brand{position:absolute;left:171px;top:62px}
.brand-name{font-size:17px;color:var(--gold);line-height:18px}
.brand-tag{font-size:9px;letter-spacing:2px;margin-top:2px;padding-left:2px}
.links{position:absolute;top:70px;list-style:none;font-size:8px;text-transform:uppercase}
.links li{height:24px;display:flex;align-items:center;gap:8px}
.links .dot{width:6px;height:6px;border-radius:50%;background:var(--white)}
.footer-rule{position:absolute;left:173px;top:226px;width:854px;height:1px;background:#333}
.legal{position:absolute;top:240px;font-size:7.5px;color:#aaa}
</style>
</head>
<body>

<section class="hero">
  <div class="hero-panel"></div>
  <h1 class="abs hero-title serif">The Seven<br><em class="gold">Principles</em></h1>
  <div class="rail" style="top:288px"><span></span><span></span><span></span><span></span><span></span><span class="on"></span><span></span><span></span></div>
  <div class="abs counter serif">1<span class="total">/7</span></div>
  <div class="arrow prev"><svg width="8" height="10" viewBox="0 0 8 10"><path d="M6 1 2 5l4 4" fill="none" stroke="#999" stroke-width="1.3"/></svg></div>
  <div class="arrow next"><svg width="8" height="10" viewBox="0 0 8 10"><path d="M2 1l4 4-4 4" fill="none" stroke="#fff" stroke-width="1.3"/></svg></div>
  <div class="hero-photo" role="img" aria-label="Crowd waving small flags in front of a domed capitol building"></div>
  <div class="numeral serif">1</div>
  <p class="quote serif">Public officials should only serve the public good. Not private interests.</p>
</section>

<section class="survey">
  <h2 class="abs survey-title serif">The <em class="gold">Survey</em></h2>
  <div class="stats">
    <div class="stat serif">82.9%*</div>
    <p style="margin-top:12px">of Americans said <strong>YES</strong> on a state ballot vote.</p>
    <p class="note">(*actual numbers will be disclosed later)</p>
    <p>We conducted a pre-registered national study<br>with X number Americans across the political spectrum</p>
    <p style="margin-top:12px">We first laid out the 7 principles. We asked if they agree?</p>
    <div class="rule"></div>
    <div class="stat serif">89.9%* said they Agree</div>
    <p style="margin-top:14px"><strong style="font-weight:600">Then we asked</strong>:<br>Would you support a legal framework built around them?</p>
    <div class="rule"></div>
    <div class="stat serif">82.9%* said yes</div>
    <p style="margin-top:16px;color:#444">14.4%* remained neutral.<br>Only 2.7%* actively opposed it.</p>
  </div>
  <div class="fade"></div>
  <div class="rail" style="top:288px"><span></span><span></span><span></span><span></span><span></span><span></span><span class="on"></span><span></span></div>
</section>

<section class="history" role="img" aria-label="Dusky sky with faint stars and a statue silhouette">
  <h2 class="history-title serif">Be Part of <em class="gold">History</em></h2>
  <p class="history-copy">For decades, we have argued over policies, parties, and ideologies. But today, across political lines, generations, and races, Americans are arriving at the same conclusion:</p>
  <p class="history-line serif">We deserve a government legally required to serve the people honestly.</p>
  <p class="history-close">And we don’t have to ask for it. We just have to vote for it.&nbsp; Be part of history. Vote now</p>
  <div class="vote-btn">Vote Now</div>
  <div class="rail" style="top:289px"><span></span><span></span><span></span><span></span><span></span><span></span><span></span><span class="on"></span></div>
</section>

<div class="strip">
  <div role="img" aria-label="Archival photo of a historic speaker" style="background:linear-gradient(#5a4e3e,#2e2820)"></div>
  <div role="img" aria-label="Archival photo of a leader at a podium" style="background:linear-gradient(#3a3632,#1c1a18)"></div>
  <div role="img" aria-label="Archival photo of a capitol dome" style="background:linear-gradient(#6a5a48,#3a3024)"></div>
  <div role="img" aria-label="Archival photo of marchers holding signs" style="background:linear-gradient(#4a4644,#242220)"></div>
  <div role="img" aria-label="Archival photo of a suffrage era portrait" style="background:linear-gradient(#8a7e70,#4e463e)"></div>
  <div role="img" aria-label="Archival photo of a civil rights activist" style="background:linear-gradient(#3e342c,#1a1612)"></div>
  <div role="img" aria-label="Archival photo of a crowd marching with banners" style="background:linear-gradient(#6e5e54,#3e2e28)"></div>
  <div role="img" aria-label="Archival photo of a civil rights leader" style="background:linear-gradient(#6a4e2e,#32241a)"></div>
  <div role="img" aria-label="Archival photo of a footprint on lunar soil" style="background:linear-gradient(#5e5a56,#2a2826)"></div>
</div>

<footer class="footer">
  <div class="brand">
    <div class="brand-name serif">Lantern Square</div>
    <div class="brand-tag">STEADY COURSE</div>
  </div>
  <ul class="links" style="left:604px"><li>Home</li><li>Mission</li><li>Who we are</li><li>Our journey</li></ul>
  <ul class="links" style="left:748px"><li>Principles</li><li>The survey</li><li class="gold">Vote now</li></ul>
  <ul class="links" style="left:892px"><li><span class="dot"></span>Townboard</li><li><span class="dot"></span>Snapframe</li><li><span class="dot"></span>Reelhouse</li></ul>
  <div class="footer-rule"></div>
  <p class="legal" style="left:173px">© Copyright 2026. Lantern Square. Steady Course. All right reserved.</p>
  <p class="legal" style="left:907px">Privacy Policy</p>
  <p class="legal" style="left:974px">Cookie Policy</p>
</footer>

</body>
</html>
```